BrightFern Life Insurance Web Design Project

We need a beautiful and simple website design to better explain our life insurance business, products and why people need life insurance.
We want the site to stand out as being simple and compelling.
As we are an old "friendly society" that has been in Australia for 130 years, we want to stand for trust, simplicity, but also longevity and security (we are supported by a global reinsurer)
We will allow customers to directly get a quote and apply for life insurance through the website.
We want a very modern look, with our exisiting gold and dark blue colours.
Target Market(s)
30-50 YOs
Industry/Entity Type
Life Insurance
Requirements
Must have
- - Life insurance quick quotation tool.
- Phone number.
- Ability to drill to information on different types of life insurance.
- Positive imagery
- our logo (refer www.brightfern-example.com.au)
Nice to have
- Target market is 30-40year olds.
Portal for advisers to access
Should not have
- Clip art
Cliched images

```html
<!DOCTYPE html>
<html lang="en">
<head>
<meta charset="utf-8">
<title>BrightFern Life Insurance</title>
<link rel="stylesheet" href="https://fonts.googleapis.com/css2?family=Fenix&family=Carlito:wght@400;700&family=Alegreya:ital,wght@1,400;1,700&display=swap">
<style>
:root{
  --purple:#372a7c;
  --gold:#d4af1f;
  --panel:#ececec;
  --header:#e9e9e9;
  --field:#9b9b9b;
  --ink:#2b2b2b;
  --white:#ffffff;
}
*{box-sizing:border-box;margin:0;padding:0}
html,body{width:1200px;height:980px;overflow:hidden;background:var(--white)}
body{position:relative;font-family:"Carlito",sans-serif;color:var(--ink)}
.abs{position:absolute}

.site-header{left:0;top:0;width:1200px;height:164px;background:var(--header);border-bottom:4px solid var(--purple);height:168px}
.brand{left:128px;top:44px;display:flex;align-items:center;gap:10px}
.brand-mark{width:26px;height:26px;background:var(--purple)}
.brand-name{font-family:"Fenix",serif;font-size:30px;color:var(--purple);line-height:1}
.phone{right:136px;top:26px;font-family:"Arial",sans-serif;font-size:20px;color:#333;display:flex;align-items:center;gap:5px}
.phone::before{content:"";width:10px;height:10px;border-radius:50%;background:var(--gold)}
.main-nav{left:128px;top:134px;width:936px;display:flex;justify-content:space-between;font-family:"Fenix",serif;font-size:18px;color:#333}

.hero-photo{left:127px;top:180px;width:565px;height:300px;background:linear-gradient(180deg,#dfe6ea 0%,#e9ecec 45%,#cfd6d4 60%,#ece7df 100%);box-shadow:1px 2px 4px rgba(0,0,0,.35);overflow:hidden}
.hero-photo svg{position:absolute;left:0;top:0}
.hero-tagline{right:14px;bottom:8px;text-align:right;font-family:"Alegreya",serif;font-style:italic;font-weight:700;font-size:31px;line-height:36px;color:var(--white)}
.slider-dots{left:387px;top:492px;display:flex;gap:5px}
.slider-dots span{width:9px;height:9px;border-radius:50%;border:1.5px solid #555;background:var(--white)}
.slider-dots span:first-child{background:#ccc}

.quote-panel{left:704px;top:180px;width:365px;height:300px;background:var(--gold);border-radius:20px;padding:34px 8px 0 4px}
.quote-title{font-family:"Alegreya",serif;font-style:italic;font-size:21px;color:#333;display:flex;align-items:center;gap:6px;margin-bottom:16px}
.quote-panel p{font-size:17px;line-height:18px;color:#222;margin-bottom:18px}
.btn-quote{right:18px;top:223px;width:159px;height:37px;background:var(--purple);color:var(--white);border-radius:6px;font-weight:700;font-size:19px;display:flex;align-items:center;justify-content:center}

.card{top:528px;width:220px;height:334px}
.card-head{height:78px;background:var(--purple);border-radius:30px 30px 0 0;color:var(--white);font-family:"Fenix",serif;font-size:20px;display:flex;align-items:center;justify-content:center;padding-top:18px}
.card-rule{height:7px;background:var(--gold)}
.card-body{height:249px;background:var(--panel);padding:20px 6px 0 11px;font-size:17px;line-height:18px;position:relative}
.card.shortcuts .card-rule{background:var(--white)}
.card.shortcuts .card-body{background:var(--gold);padding:20px 6px 0 18px}
.shortcut-list{list-style:none}
.shortcut-list li{display:flex;gap:4px;margin-bottom:10px;color:#222}
.shortcut-list svg{flex:none;margin-top:2px}
.btn-small{position:absolute;left:9px;bottom:16px;width:119px;height:28px;background:var(--gold);color:var(--white);border-radius:5px;font-weight:700;font-size:17px;display:flex;align-items:center;justify-content:center}
.field{width:203px;height:35px;background:var(--field);color:var(--white);font-family:Arial,sans-serif;font-weight:700;font-size:14px;padding:8px 10px;margin-bottom:10px;border:1px solid #c9c9c9}
.field.message{height:80px}
.card.contact .card-body{padding:8px 8px 0 8px}

.site-footer{left:0;top:890px;width:1200px;height:90px;background:var(--panel);border-top:4px solid var(--purple)}
.footer-nav{left:153px;top:7px;display:flex;font-family:"Fenix",serif;font-size:18px;color:#333}
.footer-nav span{padding:0 12px;border-left:2px solid var(--gold);line-height:26px}
.footer-nav span:first-child{padding-left:0;border-left:none}
.footer-note{left:153px;top:47px;font-size:17px;color:#333}
.social{left:936px;top:40px;display:flex;gap:16px}
.social span{width:32px;height:32px;border-radius:50%;background:#111}
</style>
</head>
<body>

<header class="site-header abs">
  <div class="brand abs"><span class="brand-mark"></span><span class="brand-name">BrightFern</span></div>
  <div class="phone abs">Tel: 1300 555 018</div>
  <nav class="main-nav abs">
    <span>Home</span><span>Choosing Life Insurance</span><span>Get Life Insurance</span><span>Claims</span><span>About Us</span>
  </nav>
</header>

<div class="hero-photo abs" role="img" aria-label="Smiling family of four walking hand in hand on a beach">
  <svg width="565" height="300" viewBox="0 0 565 300"><polygon points="348,300 565,300 565,118" fill="var(--purple)"/></svg>
  <div class="hero-tagline abs">Your<br>partner<br>for life</div>
</div>
<div class="slider-dots abs"><span></span><span></span><span></span><span></span></div>

<section class="quote-panel abs">
  <h2 class="quote-title"><svg width="16" height="14" viewBox="0 0 16 14"><path d="M0 0h7l8 7-8 7H0l8-7z" fill="var(--purple)"/></svg>Get LIfe Insurance</h2>
  <p>It is an important moment when you appreciate the value of the things in your life that really matter.</p>
  <p>Now that you have decided to get life insurance, BrightFern makes the process simple and straightforward.</p>
  <div class="btn-quote abs">Get a Quate</div>
</section>

<section class="card shortcuts abs" style="left:127px">
  <h3 class="card-head">Insurance Shortcuts</h3>
  <div class="card-rule"></div>
  <div class="card-body">
    <ul class="shortcut-list">
      <li><svg width="16" height="14" viewBox="0 0 16 14"><path d="M0 0h7l8 7-8 7H0l8-7z" fill="var(--purple)"/></svg>Life Insurance</li>
      <li><svg width="16" height="14" viewBox="0 0 16 14"><path d="M0 0h7l8 7-8 7H0l8-7z" fill="var(--purple)"/></svg>Total and permanent disablement insurance</li>
      <li><svg width="16" height="14" viewBox="0 0 16 14"><path d="M0 0h7l8 7-8 7H0l8-7z" fill="var(--purple)"/></svg>Trauma insurance</li>
      <li><svg width="16" height="14" viewBox="0 0 16 14"><path d="M0 0h7l8 7-8 7H0l8-7z" fill="var(--purple)"/></svg>Income protection insurance</li>
      <li style="margin-top:16px"><svg width="16" height="14" viewBox="0 0 16 14"><path d="M0 0h7l8 7-8 7H0l8-7z" fill="var(--purple)"/></svg>Business expenses insurance</li>
    </ul>
  </div>
</section>

<section class="card news abs" style="left:367px">
  <h3 class="card-head">Latest News</h3>
  <div class="card-rule"></div>
  <div class="card-body">
    <p>Share offer announced BrightFern has announced a non-renounceable pro rata offer of Shares each at an issue price of $0.50 to eligible shareholders on the basis of eight shares for every seven shares on 15th July 2011.</p>
    <div class="btn-small">Learn more</div>
  </div>
</section>

<section class="card why abs" style="left:607px">
  <h3 class="card-head">Why choose BrightFern</h3>
  <div class="card-rule"></div>
  <div class="card-body">
    <p>BrightFern Life Limited has more than 130 years experience as one of Australia's leading friendly societies</p>
    <div class="btn-small" style="left:12px">Learn more</div>
  </div>
</section>

<section class="card contact abs" style="left:847px">
  <h3 class="card-head">Contact an advicer</h3>
  <div class="card-rule"></div>
  <div class="card-body">
    <div class="field">Email</div>
    <div class="field">Tel</div>
    <div class="field message">Contect</div>
    <div class="btn-small">Submit</div>
  </div>
</section>

<footer class="site-footer abs">
  <nav class="footer-nav abs">
    <span>Home</span><span>Choosing Life Insurance</span><span>Get Life Insurance</span><span>Claims</span><span>About Us</span><span>Terms of Use and Privacy Policy</span>
  </nav>
  <p class="footer-note abs">Call us now on 1300 555 018 or send us an email today</p>
  <div class="social abs"><span></span><span></span><span></span></div>
</footer>

</body>
</html>
```